Business Card for a Floral & Decorating Business

I would like to take my current logo and create a better business card. I am looking for elegance as I am a florist and event decorator. My logo has multiple colour options. I like colours like green, purple, pink and orange, I think I would like a white card, open to black back ground. I want it to feel elegant and romantic. I like metallic lettering that maybe is indented in the paper, I also like glossy paper. I have a full logo already as well as a badge. I have attached both in multiple colours.m
Updates

Need extra days to review

Target Market(s)

Weddings, special events, floral customers

Industry/Entity Type

Floral and decorating

Contact Information for Business Card

Phone number, email, instagram, facebook, title, name, logo

Font styles to use
Script

Requirements
Nice to have
• Elegant

```html
<!DOCTYPE html>
<html lang="en">
<head>
<meta charset="utf-8">
<title>Wren Hollis – Business Card</title>
<link href="https://fonts.googleapis.com/css2?family=Raleway:wght@400;700&display=swap" rel="stylesheet">
<style>
  :root {
    --backdrop: #2a2a2b;
    --rose: #9e4a60;
    --ink-light: #ffffff;
    --card-black: #121212;
    --card-black-edge: #1c1c1c;
    --tile-dark: rgba(255, 255, 255, 0.035);
    --tile-edge: rgba(255, 255, 255, 0.09);
  }
  * { margin: 0; padding: 0; box-sizing: border-box; }
  html, body {
    width: 1200px;
    height: 800px;
    overflow: hidden;
    background: var(--backdrop);
    font-family: "Raleway", Arial, sans-serif;
  }
  .card {
    position: absolute;
    left: 390px;
    width: 420px;
    height: 240px;
    box-shadow: 0 12px 24px rgba(0, 0, 0, 0.45);
  }
  .card-front {
    top: 130px;
    background: var(--rose);
    color: var(--ink-light);
  }
  .brand {
    position: absolute;
    left: 26px;
    top: 108px;
    width: 166px;
    display: flex;
    align-items: center;
    justify-content: center;
    gap: 7px;
    font-weight: 400;
    font-size: 19px;
    letter-spacing: 0.5px;
  }
  .brand-dot {
    width: 8px;
    height: 8px;
    border-radius: 50%;
    background: var(--ink-light);
  }
  .divider {
    position: absolute;
    left: 209px;
    top: 81px;
    width: 1px;
    height: 79px;
    background: var(--ink-light);
  }
  .contact {
    position: absolute;
    left: 227px;
    top: 80px;
    line-height: 1;
  }
  .contact-name {
    font-weight: 700;
    font-size: 15.5px;
    letter-spacing: 0.1px;
  }
  .contact-title {
    margin-top: 4px;
    font-size: 12px;
  }
  .contact-details {
    margin-top: 12px;
    list-style: none;
    font-size: 10.8px;
  }
  .contact-details li { margin-bottom: 3.5px; }
  .card-back {
    top: 430px;
    overflow: hidden;
    background: linear-gradient(120deg, var(--card-black) 0%, var(--card-black-edge) 60%, #262626 100%);
  }
  .pattern {
    position: absolute;
    left: 4px;
    top: 4px;
    display: grid;
    grid-template-columns: repeat(10, 32px);
    grid-template-rows: repeat(4, 48px);
    column-gap: 10px;
    row-gap: 14px;
  }
  .tile {
    border-radius: 3px;
    background: var(--tile-dark);
    border: 1px solid var(--tile-edge);
  }
  .tile:nth-child(10n+7), .tile:nth-child(10n+8) { border-color: rgba(255,255,255,0.13); }
  .tile:nth-child(10n+9), .tile:nth-child(10n) { border-color: rgba(255,255,255,0.18); background: rgba(255,255,255,0.06); }
  .tile.tile-accent {
    background: var(--rose);
    border-color: var(--rose);
  }
</style>
</head>
<body>
  <section class="card card-front">
    <div class="brand"><span class="brand-dot"></span><span class="brand-name">Wren Hollis</span></div>
    <div class="divider"></div>
    <div class="contact">
      <p class="contact-name">JORDAN ASHBY</p>
      <p class="contact-title">President &amp; CEO</p>
      <ul class="contact-details">
        <li>000-000-0000</li>
        <li>j.ashby@wrenhollis-events.com</li>
        <li>www.wrenhollis-events.com</li>
      </ul>
    </div>
  </section>
  <section class="card card-back" role="img" aria-label="Black card back with a repeating embossed floral monogram pattern and one rose accent">
    <div class="pattern">
      <div class="tile"></div><div class="tile"></div><div class="tile"></div><div class="tile"></div><div class="tile"></div>
      <div class="tile"></div><div class="tile"></div><div class="tile"></div><div class="tile"></div><div class="tile"></div>
      <div class="tile"></div><div class="tile"></div><div class="tile"></div><div class="tile"></div><div class="tile"></div>
      <div class="tile"></div><div class="tile"></div><div class="tile"></div><div class="tile"></div><div class="tile"></div>
      <div class="tile"></div><div class="tile"></div><div class="tile"></div><div class="tile"></div><div class="tile"></div>
      <div class="tile"></div><div class="tile"></div><div class="tile"></div><div class="tile tile-accent"></div><div class="tile"></div>
      <div class="tile"></div><div class="tile"></div><div class="tile"></div><div class="tile"></div><div class="tile"></div>
      <div class="tile"></div><div class="tile"></div><div class="tile"></div><div class="tile"></div><div class="tile"></div>
    </div>
  </section>
</body>
</html>
```